Up to the Challenge - PPT Template with Splash Slide

We are looking for a PPT template that has 4 slides.
1. Splash slide (Creative, fun, no content, a visual representation of the theme)
2. Section header slide
3. Content Slide
4. Content Slide, another design option
The theme is 'UP to the Challenge'. The design should reflect this theme.
The colors should be in Purple (#864B99), Blue (#0A80C2), and Green (#52B054).

```html
<!DOCTYPE html>
<html lang="en">
<head>
<meta charset="utf-8">
<title>Up to the Challenge – Template Slides</title>
<link href="https://fonts.googleapis.com/css2?family=Montserrat:wght@400;500;600;700&display=swap" rel="stylesheet">
<style>
  :root{
    --purple:#864b99;
    --purple-soft:#a46bb8;
    --blue:#0a80c2;
    --green:#52b054;
    --slate:#33424d;
    --paper:#f7f7f7;
    --white:#ffffff;
    --canvas:#d9d9d9;
    --body-grey:#6b6f73;
  }
  *{box-sizing:border-box;margin:0;padding:0}
  html,body{width:1200px;height:1059px;overflow:hidden}
  body{background:var(--canvas);font-family:'Montserrat',sans-serif;position:relative}
  .slide{position:absolute;width:540px;height:304px;overflow:hidden}
  .slide > svg.shapes{position:absolute;inset:0;width:540px;height:304px}
  .col-left{left:32px}.col-right{left:628px}
  .row-1{top:23px}.row-2{top:377px}.row-3{top:731px}
  .dark{background:var(--slate)}
  .light{background:var(--paper)}
  .white{background:var(--white)}
  .green{background:var(--green)}
  .abs{position:absolute}
  .title{font-weight:600;font-size:22.5px;line-height:27px;letter-spacing:.3px;color:var(--slate)}
  .title.on-dark{color:var(--white)}
  .subtitle{font-weight:600;font-size:10px;color:var(--purple);letter-spacing:.2px}
  .body{font-size:8.9px;line-height:10.9px;color:var(--body-grey)}
  .body.on-dark{color:var(--white)}
  .checks{list-style:none;font-size:8.9px;line-height:10.9px;color:var(--purple)}
  .checks li::before{content:"✓";display:inline-block;width:12px}
  .date-pill{background:var(--green);color:var(--white);font-size:8px;border-radius:9px;width:92px;height:17px;line-height:17px;text-align:center}
  .accent-bar{background:var(--green);width:66px;height:4px}
  .photo{background:linear-gradient(135deg,#8c7b6e,#c9c4bd 45%,#6f655c)}
  .card{position:absolute;width:154px;height:91px;border-radius:5px;padding:14px 13px;color:var(--white)}
  .card h3{font-size:8.8px;font-weight:700;letter-spacing:.2px;margin-bottom:9px}
  .card p{font-size:7.6px;line-height:9.3px}
  .card.purple{background:var(--purple-soft)}
  .card.green{background:var(--green)}
  .card.blue{background:var(--blue)}
  .card.chart{background:var(--white);padding:0}
  .panel-item{position:absolute;left:372px;color:var(--white);width:150px}
  .panel-item h4{font-size:8px;font-weight:700;position:relative}
  .panel-item h4::before{content:"•";position:absolute;left:-12px}
  .panel-item p{font-size:6.8px;line-height:8.2px;margin-top:3px}
</style>
</head>
<body>

<!-- Splash -->
<section class="slide dark col-left row-1">
  <svg class="shapes" viewBox="0 0 540 304">
    <circle cx="438" cy="88" r="80" fill="none" stroke="var(--blue)" stroke-width="46"/>
    <circle cx="0" cy="258" r="31" fill="var(--purple)"/>
  </svg>
  <div class="abs" role="img" aria-label="Illustration of a businessman running up rising bar charts with a flag, breaking a finish ribbon, surrounded by gears and goal icons" style="left:240px;top:66px;width:290px;height:238px;border-radius:40% 40% 0 0;background:radial-gradient(ellipse at 55% 60%,rgba(158,169,243,.55) 0%,rgba(60,90,190,.35) 45%,rgba(51,66,77,0) 75%)"></div>
  <div class="abs accent-bar" style="left:31px;top:35px"></div>
  <h1 class="abs title on-dark" style="left:31px;top:48px">PRESENTATION<br>TITLE HERE</h1>
  <p class="abs body on-dark" style="left:31px;top:106px;width:222px">Lorem ipsum dolor sit amet, consectetuer adipiscing elit. Maecenas porttitor congue massa. Fusce posuere, magna sed pulvinar ultricies, purus lectus malesuada libero, sit amet commodo magna eros quis urna.</p>
  <div class="abs date-pill" style="left:31px;top:182px">22 March 2022</div>
</section>

<!-- Content with round photo -->
<section class="slide light col-right row-1">
  <svg class="shapes" viewBox="0 0 540 304">
    <circle cx="488" cy="73" r="204" fill="var(--blue)"/>
    <circle cx="42" cy="305" r="43" fill="var(--green)"/>
  </svg>
  <div class="abs photo" role="img" aria-label="Photo of colleagues meeting around a table with laptops" style="left:307px;top:-120px;width:390px;height:384px;border-radius:50%;"></div>
  <p class="abs subtitle" style="left:43px;top:60px">SUB-TITLE HERE</p>
  <h2 class="abs title" style="left:40px;top:77px">PRESENTATION<br>TITLE HERE</h2>
  <p class="abs body" style="left:43px;top:143px;width:252px">Lorem ipsum dolor sit amet, consectetuer adipiscing elit. Maecenas porttitor congue massa. Fusce posuere, magna sed pulvinar ultricies, purus lectus malesuada libero, sit amet commodo magna eros quis urna.</p>
  <ul class="abs checks" style="left:43px;top:201px">
    <li>Maecenas porttitor congue massa.</li>
    <li>Maecenas porttitor congue massa.</li>
    <li>Maecenas porttitor congue massa.</li>
  </ul>
</section>

<!-- Section break -->
<section class="slide green col-left row-2">
  <svg class="shapes" viewBox="0 0 540 304">
    <circle cx="-60" cy="152" r="312" fill="var(--purple)"/>
    <circle cx="-60" cy="152" r="202" fill="var(--green)"/>
  </svg>
  <h2 class="abs title on-dark" style="left:160px;top:127px;font-size:21.5px;line-height:25px">SLIDE<br>BREAK</h2>
  <p class="abs body on-dark" style="left:272px;top:125px;width:205px">Lorem ipsum dolor sit amet, consectetuer adipiscing elit. Maecenas porttitor congue massa. Fusce posuere, magna sed pulvinar ultricies, purus lectus malesuada libero, sit amet commodo magna eros quis urna.</p>
</section>

<!-- Content with side panel -->
<section class="slide white col-right row-2">
  <svg class="shapes" viewBox="0 0 540 304">
    <circle cx="0" cy="258" r="31" fill="var(--blue)"/>
    <rect x="333" y="133" width="207" height="171" fill="var(--green)"/>
  </svg>
  <div class="abs photo" role="img" aria-label="Photo of a presenter at a whiteboard with a team at desks" style="left:333px;top:0;width:207px;height:133px;background:linear-gradient(160deg,#e6e6e4,#b9b8b5 50%,#4d4c4a)"></div>
  <p class="abs subtitle" style="left:47px;top:61px">SUB-TITLE HERE</p>
  <h2 class="abs title" style="left:44px;top:78px">PRESENTATION<br>TITLE HERE</h2>
  <p class="abs body" style="left:47px;top:144px;width:252px">Lorem ipsum dolor sit amet, consectetuer adipiscing elit. Maecenas porttitor congue massa. Fusce posuere, magna sed pulvinar ultricies, purus lectus malesuada libero, sit amet commodo magna eros quis urna.</p>
  <ul class="abs checks" style="left:47px;top:203px">
    <li>Maecenas porttitor congue massa.</li>
    <li>Maecenas porttitor congue massa.</li>
    <li>Maecenas porttitor congue massa.</li>
  </ul>
  <div class="panel-item" style="top:155px">
    <h4>SLIDE TITLE TEXT HERE</h4>
    <p>Lorem ipsum dolor sit amet, consectetuer adipiscing elit. Maecenas porttitor congue massa.</p>
  </div>
  <div class="panel-item" style="top:210px">
    <h4>SLIDE TITLE TEXT HERE</h4>
    <p>Lorem ipsum dolor sit amet, consectetuer adipiscing elit. Maecenas porttitor congue massa.</p>
  </div>
</section>

<!-- Card grid -->
<section class="slide dark col-left row-3">
  <h2 class="abs on-dark" style="left:35px;top:64px;font-size:10.5px;font-weight:700;color:var(--white)">SLIDE TITLE TEXT HERE</h2>
  <p class="abs body on-dark" style="left:35px;top:104px;width:145px;font-size:9.4px;line-height:11px">Lorem ipsum dolor sit amet, consectetuer adipiscing elit. Maecenas porttitor congue massa. Fusce posuere, magna sed pulvinar ultricies, purus lectus malesuada libero, sit amet commodo magna eros quis urna.</p>

  <div class="card purple" style="left:194px;top:61px">
    <h3>SLIDE TITLE TEXT HERE</h3>
    <p>Lorem ipsum dolor sit amet, consectetuer adipiscing elit. Maecenas porttitor congue massa.</p>
  </div>
  <div class="card green" style="left:355px;top:61px">
    <h3>SLIDE TITLE TEXT HERE</h3>
    <p>Lorem ipsum dolor sit amet, consectetuer adipiscing elit. Maecenas porttitor congue massa.</p>
  </div>
  <div class="card blue" style="left:194px;top:159px">
    <h3>SLIDE TITLE TEXT HERE</h3>
    <p>Lorem ipsum dolor sit amet, consectetuer adipiscing elit. Maecenas porttitor congue massa.</p>
    <svg class="abs" style="left:127px;top:68px" width="15" height="14" viewBox="0 0 15 14">
      <path d="M1 1v12h13" fill="none" stroke="#fff" stroke-width="1.4"/>
      <rect x="4" y="7" width="2" height="5" fill="#fff"/><rect x="7.5" y="4" width="2" height="8" fill="#fff"/><rect x="11" y="2" width="2" height="10" fill="#fff"/>
    </svg>
  </div>
  <div class="card chart" style="left:355px;top:159px">
    <svg width="154" height="91" viewBox="0 0 154 91" font-family="Montserrat, sans-serif">
      <text x="77" y="16" font-size="5.5" text-anchor="middle" fill="#595959">Chart Title</text>
      <g stroke="#e3e3e3" stroke-width=".5">
        <line x1="17" y1="24" x2="143" y2="24"/><line x1="17" y1="32" x2="143" y2="32"/><line x1="17" y1="40" x2="143" y2="40"/>
        <line x1="17" y1="48" x2="143" y2="48"/><line x1="17" y1="56" x2="143" y2="56"/><line x1="17" y1="64" x2="143" y2="64"/>
      </g>
      <line x1="17" y1="72" x2="143" y2="72" stroke="#bfbfbf" stroke-width=".6"/>
      <g font-size="4" fill="#7f7f7f" text-anchor="end">
        <text x="14" y="26">6</text><text x="14" y="34">5</text><text x="14" y="42">4</text><text x="14" y="50">3</text><text x="14" y="58">2</text><text x="14" y="66">1</text><text x="14" y="74">0</text>
      </g>
      <g>
        <rect x="24" y="37" width="6" height="35" fill="var(--purple)"/><rect x="31" y="53" width="6" height="19" fill="var(--green)"/><rect x="38" y="56" width="6" height="16" fill="var(--blue)"/>
        <rect x="55" y="52" width="6" height="20" fill="var(--purple)"/><rect x="62" y="36" width="6" height="36" fill="var(--green)"/><rect x="69" y="56" width="6" height="16" fill="var(--blue)"/>
        <rect x="86" y="44" width="6" height="28" fill="var(--purple)"/><rect x="93" y="58" width="6" height="14" fill="var(--green)"/><rect x="100" y="48" width="6" height="24" fill="var(--blue)"/>
        <rect x="117" y="36" width="6" height="36" fill="var(--purple)"/><rect x="124" y="50" width="6" height="22" fill="var(--green)"/><rect x="131" y="32" width="6" height="40" fill="var(--blue)"/>
      </g>
      <g font-size="3.8" fill="#7f7f7f" text-anchor="middle">
        <text x="34" y="80">Category 1</text><text x="65" y="80">Category 2</text><text x="96" y="80">Category 3</text><text x="127" y="80">Category 4</text>
      </g>
    </svg>
  </div>

  <p class="abs" style="left:35px;top:279px;font-size:8.4px;color:var(--white)">do not distributed</p>
  <svg class="abs" style="left:117px;top:276px" width="390" height="16" viewBox="0 0 390 16">
    <line x1="0" y1="8" x2="367" y2="8" stroke="#ffffff" stroke-width=".6" stroke-dasharray="3 2" opacity=".8"/>
    <circle cx="380" cy="8" r="7.5" fill="#ffffff"/>
    <text x="380" y="10.8" font-size="7.5" text-anchor="middle" fill="var(--slate)" font-family="Montserrat, sans-serif">1</text>
  </svg>
</section>

<!-- Content with device -->
<section class="slide light col-right row-3">
  <svg class="shapes" viewBox="0 0 540 304">
    <circle cx="538" cy="152" r="194" fill="var(--purple)"/>
    <circle cx="523" cy="152" r="89" fill="var(--green)"/>
    <circle cx="18" cy="304" r="42" fill="var(--blue)"/>
  </svg>
  <div class="abs" role="img" aria-label="Laptop showing a contacts app screen" style="left:285px;top:96px;width:195px;height:111px;border-radius:6px 6px 2px 2px;background:linear-gradient(180deg,#2b2f36 0%,#e9edf3 12%,#dfe5ee 88%,#9da3ab 100%)"></div>
  <p class="abs subtitle" style="left:47px;top:61px">SUB-TITLE HERE</p>
  <h2 class="abs title" style="left:44px;top:78px">PRESENTATION<br>TITLE HERE</h2>
  <p class="abs body" style="left:47px;top:144px;width:200px">Lorem ipsum dolor sit amet, consectetuer adipiscing elit. Maecenas porttitor congue massa. Fusce posuere, magna sed pulvinar ultricies, purus lectus malesuada libero, sit amet commodo magna eros quis urna.</p>
  <ul class="abs checks" style="left:47px;top:207px">
    <li>Maecenas porttitor congue massa.</li>
    <li>Maecenas porttitor congue massa.</li>
    <li>Maecenas porttitor congue massa.</li>
  </ul>
</section>

</body>
</html>
```